Environmental Consultancey needs Web Design

A consultancey firm based in Papua New Guinea specialising servicing a client market primarily in Melanesia, the wider Pacific Region and South East Asia. The firm provides services to community development and resource extraction activites that incorporate sustainable livelihoods for local customary land owners with environmentally responsibile practices and a focus on maintaining biodiversity and ecosystem services. We aim to encompass Culture, Custom and Science in our approach. Our website preferentially will convey a relaxed Pacific Island feel in its colours and design rather than a sterile corporate feel. See attached logo that will need to be visible on page or which may provide basis for ideas for the page.

Target Market(s)

Our target market is primarily the oil, gas and mining industry, secondarily international donor and aid programs followed by government projects and not for profit programs. Services include:
1. Biodiversity and Conservation - Fauna and Flora survey, assessment, management, monitoring & research, protected areas & endangered & threatend species.
2. Social & Community - impact, stakeholder engagement, census and survey, land and community affairs, capacity building empowerment.
3. Environmental Management - sustainable use, enterprise development & management, biodiversity offsets.

Industry/Entity Type

Community

Requirements
Must have
• Multiple pages, Logo somewhere on home page. Space for a couple of photos that as yet ive not decieded upon.
Nice to have
• Perhaps incorporate shapes, texture and colours that convey a feel of the attached photo of a blue bird of paradise. The blue fine overlapping and interlocking feather patterns are appealing perhaps as a background and the other colours used in boarders ? Abstract is fine as would be symbolic images or tribal ambience. The company is all about blending humanity in all its forms with the environment.

```html
<!DOCTYPE html>
<html lang="en">
<head>
<meta charset="utf-8">
<title>Reefline Environs</title>
<link rel="stylesheet" href="https://fonts.googleapis.com/css2?family=Open+Sans:wght@400;600&family=Dosis:wght@400;500&family=Arimo:wght@400&display=swap">
<style>
:root{
  --sand:#ddd3c2;
  --tan:#d8c9ab;
  --paper:#f7f5f1;
  --teal:#5ab8b0;
  --teal-top:#3f9e96;
  --teal-text:#1f6e66;
  --olive:#7f9a2a;
  --olive-top:#5c7612;
  --olive-text:#4f6410;
  --slider-green:#5fb87f;
  --slider-dark:#231f20;
  --arrow:#d6e23a;
  --rule:#6b7a2a;
  --welcome:#f2ec8c;
  --welcome-head:#1e9c4a;
  --footer:#698b6c;
  --field:#7fa283;
  --submit:#2a9c52;
  --ink:#3a3a3a;
}
*{box-sizing:border-box;margin:0;padding:0}
html,body{width:1077px;height:1200px;overflow:hidden;background:var(--sand)}
body{font-family:"Open Sans",Verdana,sans-serif;color:var(--ink)}
.page{position:absolute;left:0;top:0;width:1049px;height:1169px;transform-origin:0 0;transform:scale(1.0267,1.0265);background:var(--sand)}
.sheet{position:absolute;left:22px;top:15px;width:1003px;height:1154px;
  background:radial-gradient(ellipse at 30% 75%,rgba(170,190,160,.35),transparent 55%),radial-gradient(ellipse at 75% 60%,rgba(180,195,170,.3),transparent 50%),var(--paper)}
.topband{position:absolute;left:0;top:30px;width:1049px;height:57px;background:var(--tan)}
.brand{position:absolute;left:32px;top:28px;width:178px;height:177px;background:#fff;display:flex;flex-direction:column;align-items:center;justify-content:center;gap:8px}
.brand-dot{width:22px;height:22px;border-radius:50%;background:var(--teal)}
.brand-name{font-size:19px;font-weight:600;color:#2b2b2b;text-align:center;line-height:1.15}
.search{position:absolute;left:581px;top:41px;width:221px;height:33px;background:#ede9e1;display:flex;align-items:center;padding-left:16px;font-size:13px;color:#8a8a8a}
.search svg{position:absolute;right:8px;top:5px}
.follow{position:absolute;left:841px;top:50px;font-size:11px;color:#333;display:flex;align-items:center;gap:5px}
.follow .social{width:21px;height:21px;display:inline-block}
.nav{position:absolute;left:226px;top:103px;display:flex}
.nav-btn{width:95.6px;text-align:center}
.nav-tile{height:75px;display:flex;align-items:center;justify-content:center;border-top:12px solid var(--teal-top);background:var(--teal)}
.nav-btn.olive .nav-tile{background:var(--olive);border-top-color:var(--olive-top)}
.nav-btn:nth-child(2) .nav-tile{background:#7fd3cb}
.nav-btn:nth-child(4) .nav-tile{background:#3e958e}
.nav-btn:nth-child(7) .nav-tile{background:#6b8423}
.nav-label{font-family:"Arimo",Arial,sans-serif;font-size:17px;margin-top:4px;color:var(--teal-text)}
.nav-btn:nth-child(2) .nav-label{color:#4da79f}
.nav-btn:nth-child(4) .nav-label{color:#123f3b}
.nav-btn.olive .nav-label{color:var(--olive-text)}
.nav-btn:nth-child(5) .nav-label{color:#6f8d1a}
.hero{position:absolute;left:54px;top:237px;width:537px;height:363px;border:2px solid #2c2c2c;
  background:linear-gradient(160deg,#9fc7b4 0%,#3f8f88 30%,#2e6fae 55%,#1f5f8f 70%,#8ab59a 100%)}
.hero-caption{position:absolute;left:0;bottom:0;width:100%;height:62px;background:rgba(40,40,40,.72);color:#fff;font-family:"Dosis",sans-serif;font-size:27px;display:flex;align-items:center;padding-left:18px}
.sliders{position:absolute;left:592px;top:237px;width:405px;height:363px;background:var(--slider-green);box-shadow:0 14px 18px -10px rgba(0,0,0,.35)}
.slide{position:absolute;left:4px;width:397px;height:80px;padding:10px 0 0 49px;color:#fff}
.slide.active{background:var(--slider-dark)}
.slide + .slide{border-top:2px dotted rgba(40,90,60,.5)}
.slide h3{font-weight:400;font-size:23px;line-height:1.1}
.slide p{font-size:12px;line-height:15px;margin-top:3px}
.slide svg{position:absolute;left:12px;top:30px}
.rule{position:absolute;left:73px;top:635px;width:902px;height:2px;background:var(--rule)}
.welcome{position:absolute;left:48px;top:668px;width:439px;height:245px;background:var(--welcome);border-radius:9px;padding:14px 36px 0 35px}
.welcome h2{font-weight:400;font-size:25px;color:var(--welcome-head);margin-left:3px}
.welcome p{font-size:12px;line-height:17px;text-align:justify;color:#333;margin-top:6px}
.projects-title{position:absolute;left:513px;top:656px;font-size:21px;font-weight:400;color:#333}
.projects{position:absolute;left:519px;top:693px;display:grid;grid-template-columns:repeat(3,158px);grid-template-rows:repeat(2,107px);gap:5px 6px}
.project-photo{border:1px solid #555}
.tone-a{background:linear-gradient(150deg,#7fc0b0,#2d7fb8 45%,#1b5a8c 70%,#7aa88e)}
.tone-b{background:linear-gradient(150deg,#8a6b3a,#2a6a8a 45%,#143c5a 65%,#9b8050)}
.footer{position:absolute;left:0;top:938px;width:1049px;height:231px;background:var(--footer);color:#eef3ee;font-size:13px}
.footer ul{list-style:none;position:absolute;top:31px;line-height:15.5px}
.footer .copy{position:absolute;left:49px;top:194px}
.form{position:absolute;left:708px;top:6px;width:252px}
.form-title{font-size:13px;margin-bottom:6px}
.field{height:30px;background:var(--field);margin-bottom:5px;padding:7px 11px;font-size:13px;color:#e4ede4}
.field.tall{height:56px}
.submit{position:absolute;left:888px;top:198px;width:71px;height:26px;background:linear-gradient(#3bb866,var(--submit));color:#fff;font-size:13px;display:flex;align-items:center;justify-content:center}
</style>
</head>
<body>
<div class="page">
  <div class="sheet"></div>
  <div class="topband"></div>
  <div class="brand"><span class="brand-dot"></span><span class="brand-name">Reefline<br>Environs</span></div>
  <div class="search">Search
    <svg width="30" height="24" viewBox="0 0 30 24"><circle cx="11" cy="10" r="7" fill="none" stroke="#777" stroke-width="2.5"/><line x1="16" y1="15" x2="26" y2="22" stroke="#777" stroke-width="4" stroke-linecap="round"/></svg>
  </div>
  <div class="follow">Follow Us on :
    <span class="social" style="background:#1a7bb8" role="img" aria-label="Professional network"></span>
    <span class="social" style="background:#35b3e4" role="img" aria-label="Microblog"></span>
    <span class="social" style="background:#3b5b9a" role="img" aria-label="Social network"></span>
  </div>

  <nav class="nav">
    <div class="nav-btn"><div class="nav-tile"><svg width="46" height="46" viewBox="0 0 46 46" fill="none" stroke="#fff" stroke-width="3"><rect x="4" y="4" width="38" height="30" rx="4"/><path d="M14 34l-3 9 10-9"/><circle cx="23" cy="15" r="5"/><path d="M14 29c1-6 17-6 18 0"/></svg></div><div class="nav-label">Button 2</div></div>
    <div class="nav-btn"><div class="nav-tile"><svg width="46" height="46" viewBox="0 0 46 46" fill="none" stroke="#fff" stroke-width="3"><path d="M4 22L23 5l19 17"/><path d="M10 17v24h26V17"/><rect x="18" y="24" width="10" height="10"/></svg></div><div class="nav-label">Button 3</div></div>
    <div class="nav-btn"><div class="nav-tile"><svg width="46" height="46" viewBox="0 0 46 46" fill="none" stroke="#fff" stroke-width="3"><rect x="4" y="4" width="38" height="30" rx="4"/><path d="M14 34l-3 9 10-9"/><circle cx="23" cy="15" r="5"/><path d="M14 29c1-6 17-6 18 0"/></svg></div><div class="nav-label">Button 4</div></div>
    <div class="nav-btn"><div class="nav-tile"><svg width="46" height="46" viewBox="0 0 46 46" fill="none" stroke="#fff" stroke-width="3"><path d="M20 8c-9 0-15 5-15 11 0 3 2 6 4 8l-2 7 8-4"/><rect x="15" y="14" width="27" height="22" rx="8"/><path d="M21 21h15M21 26h15M21 31h10"/></svg></div><div class="nav-label">Button 5</div></div>
    <div class="nav-btn olive"><div class="nav-tile"><svg width="46" height="46" viewBox="0 0 46 46" fill="none" stroke="#fff" stroke-width="3"><path d="M4 22L23 5l19 17"/><path d="M10 17v24h26V17"/><rect x="18" y="24" width="10" height="10"/></svg></div><div class="nav-label">Button 6</div></div>
    <div class="nav-btn olive"><div class="nav-tile"><svg width="46" height="46" viewBox="0 0 46 46" fill="none" stroke="#fff" stroke-width="3"><rect x="4" y="4" width="38" height="30" rx="4"/><path d="M14 34l-3 9 10-9"/><circle cx="23" cy="15" r="5"/><path d="M14 29c1-6 17-6 18 0"/></svg></div><div class="nav-label">Button 7</div></div>
    <div class="nav-btn olive"><div class="nav-tile"><svg width="46" height="46" viewBox="0 0 46 46" fill="none" stroke="#fff" stroke-width="3"><path d="M20 8c-9 0-15 5-15 11 0 3 2 6 4 8l-2 7 8-4"/><rect x="15" y="14" width="27" height="22" rx="8"/><path d="M21 21h15M21 26h15M21 31h10"/></svg></div><div class="nav-label">Button 8</div></div>
    <div class="nav-btn olive"><div class="nav-tile"><svg width="46" height="46" viewBox="0 0 46 46" fill="none" stroke="#fff" stroke-width="3"><rect x="4" y="4" width="38" height="30" rx="4"/><path d="M14 34l-3 9 10-9"/><circle cx="23" cy="15" r="5"/><path d="M14 29c1-6 17-6 18 0"/></svg></div><div class="nav-label">Button 9</div></div>
  </nav>

  <div class="hero" role="img" aria-label="Blue bird of paradise hanging from a branch">
    <div class="hero-caption">" Encompassing Culture, Custom &amp; Science "</div>
  </div>
  <div class="sliders">
    <div class="slide active" style="top:6px"><svg width="22" height="26" viewBox="0 0 22 26" fill="none" stroke="var(--arrow)" stroke-width="2"><path d="M12 2L3 13l9 11M19 2L10 13l9 11"/></svg><h3>Slider 1</h3><p>The atmosphere of the Earth serves as a key factor in sustaining the planetary ecosystem.</p></div>
    <div class="slide" style="top:90px"><svg width="22" height="26" viewBox="0 0 22 26" fill="none" stroke="var(--arrow)" stroke-width="2"><path d="M12 2L3 13l9 11M19 2L10 13l9 11"/></svg><h3>Slider 2</h3><p>The atmosphere of the Earth serves as a key factor in sustaining the planetary ecosystem.</p></div>
    <div class="slide" style="top:178px"><svg width="22" height="26" viewBox="0 0 22 26" fill="none" stroke="var(--arrow)" stroke-width="2"><path d="M12 2L3 13l9 11M19 2L10 13l9 11"/></svg><h3>Slider 3</h3><p>The atmosphere of the Earth serves as a key factor in sustaining the planetary ecosystem.</p></div>
    <div class="slide" style="top:265px;padding-top:18px"><svg width="22" height="26" viewBox="0 0 22 26" fill="none" stroke="var(--arrow)" stroke-width="2"><path d="M12 2L3 13l9 11M19 2L10 13l9 11"/></svg><h3>Slider 4</h3><p>The atmosphere of the Earth serves as a key factor in sustaining the planetary ecosystem.</p></div>
  </div>

  <div class="rule"></div>

  <section class="welcome">
    <h2>Welcome!</h2>
    <p>The potential dangers of global warming are being increasingly studied by a wide global consortium of scientists. These scientists are increasingly concerned about the potential long-term effects of global warming on our natural environment and on the planet. Of particular concern is how climate change and global warming caused by anthropogenic, or human-made releases of greenhouse gases, most notably carbon dioxide, can act interactively, and have adverse effects upon the planet, its natural environment and humans' existence.</p>
  </section>

  <h2 class="projects-title">Our Projects</h2>
  <div class="projects">
    <div class="project-photo tone-a" role="img" aria-label="Project photo: blue bird of paradise"></div>
    <div class="project-photo tone-b" role="img" aria-label="Project photo: bird of paradise in display"></div>
    <div class="project-photo tone-a" role="img" aria-label="Project photo: blue bird of paradise"></div>
    <div class="project-photo tone-a" role="img" aria-label="Project photo: blue bird of paradise"></div>
    <div class="project-photo tone-b" role="img" aria-label="Project photo: bird of paradise in display"></div>
    <div class="project-photo tone-a" role="img" aria-label="Project photo: blue bird of paradise"></div>
  </div>

  <footer class="footer">
    <ul style="left:59px"><li>Button 1</li><li>Button 2</li><li>Button 3</li><li>Button 4</li><li>Button 5</li><li>Button 6</li><li>Button 7</li><li>Button 8</li></ul>
    <ul style="left:217px"><li>Button 1</li><li>Button 2</li><li>Button 3</li><li>Button 4</li><li>Button 5</li><li>Button 6</li><li>Button 7</li><li>Button 8</li></ul>
    <ul style="left:441px"><li>Contact Info</li><li>Addres Details</li><li>Telephone No.</li><li>Fax No.</li><li>Email id:</li></ul>
    <div class="form">
      <div class="form-title">Queries / Comments</div>
      <div class="field">Name</div>
      <div class="field">Contact No.</div>
      <div class="field">Email id</div>
      <div class="field tall">Comments</div>
    </div>
    <div class="submit">Submit</div>
    <div class="copy">Copyright All right reserved</div>
  </footer>
</div>
</body>
</html>
```